Business Card Design Project - IT Company

Kestrafield Information Technology Solutions
We are an Information Technology Company. We provide computer services to commercial companies. We would like a new card full color front and back with bleeding edge.
We have a logo that you can use or if you want to come up with a new logo that is fine too.
Our colors are mostly Maroon and black but be creative.
Sample Information
Brent R Okafor
4812 W Saguaro Ridge Drive
Suite 600
Phoenix, AZ 85016
O: 602.914.2037
C: 602.468.1290
24/7: 888.914.2037
bokafor@kestrafield.example
www.kestrafield.example
Target Market(s)
Business of all sizes
Industry/Entity Type
Computer
Requirements
Must have
- Bleeding edge
full color on both sides

```html
<!DOCTYPE html>
<html lang="en">
<head>
<meta charset="utf-8">
<title>Kestrafield Business Card</title>
<link rel="stylesheet" href="https://fonts.googleapis.com/css2?family=Open+Sans:wght@400;700&display=swap">
<style>
  :root {
    --maroon: #86000b;
    --maroon-deep: #5e0008;
    --paper: #ffffff;
    --ink: #2b2b2b;
    --backdrop: #e4e4e4;
  }
  * { box-sizing: border-box; margin: 0; padding: 0; }
  html, body { width: 1200px; height: 900px; overflow: hidden; }
  body {
    background: var(--backdrop);
    font-family: "Open Sans", Arial, sans-serif;
    position: relative;
  }
  .card {
    position: absolute;
    width: 560px;
    height: 320px;
    background: var(--paper);
    overflow: hidden;
  }
  .card-front { left: 190px; top: 80px; }
  .card-back { left: 450px; top: 480px; }

  .band {
    position: absolute;
    left: 0;
    width: 100%;
    height: 58px;
    background: var(--maroon);
  }
  .band-top { top: 0; }
  .band-bottom { bottom: 0; }

  .wordmark {
    position: absolute;
    color: var(--ink);
    font-weight: 400;
    line-height: 1.1;
  }
  .wordmark .name {
    display: block;
    letter-spacing: 6px;
    text-transform: uppercase;
  }
  .wordmark .tagline { display: block; }

  .card-front .wordmark {
    left: 0; right: 0;
    top: 118px;
    text-align: center;
  }
  .card-front .wordmark .name { font-size: 44px; }
  .card-front .wordmark .tagline { font-size: 19px; margin-top: 4px; }

  .card-back .wordmark {
    left: 28px;
    top: 130px;
  }
  .card-back .wordmark .name { font-size: 30px; letter-spacing: 4px; }
  .card-back .wordmark .tagline { font-size: 13px; margin-top: 3px; }

  .back-panel {
    position: absolute;
    inset: 0;
    width: 560px;
    height: 320px;
  }
  .contact {
    position: absolute;
    left: 318px;
    top: 104px;
    color: var(--paper);
    font-size: 12.5px;
    line-height: 1.32;
  }
  .contact .person {
    font-size: 18px;
    font-weight: 700;
    margin-bottom: 6px;
  }
</style>
</head>
<body>

  <section class="card card-front" aria-label="Card front">
    <div class="band band-top"></div>
    <div class="wordmark">
      <span class="name">Kestrafield</span>
      <span class="tagline">Information Technology Solutions</span>
    </div>
    <div class="band band-bottom"></div>
  </section>

  <section class="card card-back" aria-label="Card back">
    <svg class="back-panel" viewBox="0 0 560 320" aria-hidden="true">
      <path d="M 262 0 Q 318 170 212 320 L 204 320 Q 308 170 252 0 Z" fill="var(--maroon-deep)"/>
      <path d="M 262 0 Q 318 170 212 320 L 560 320 L 560 0 Z" fill="var(--maroon)"/>
    </svg>
    <div class="wordmark">
      <span class="name">Kestrafield</span>
      <span class="tagline">Information Technology Solutions</span>
    </div>
    <address class="contact">
      <p class="person">Brent R Okafor</p>
      <p>4812 W Saguaro Ridge Drive</p>
      <p>Suite 600</p>
      <p>Phoenix, AZ 85016</p>
      <p>O: 602.914.2037</p>
      <p>C: 602.468.1290</p>
      <p>24/7: 888.914.2037</p>
      <p>bokafor@kestrafield.example</p>
      <p>www.kestrafield.example</p>
    </address>
  </section>

</body>
</html>
```